Plumweave Inc. Website & Korvix Apps Landing Pages

We need a web site design for our company. We develop software and do various consultant projects for our clients. Our products focus on the mobile platform, mainly the Korvix (business, games, social, etc.). We want to communicate that our software is simple and good as candy. The web pages should be fun to look at not loosing seriousness and credibility. Web 2.0 style and 960 grid system a must. We are opened to any overall site colour scheme suggestions (look at the sites we like below).

Must haves:
- Our logo should be seen on the site and look great on it :-) (preview attached below)
- Main home page and app landing page.
- Section links/tabs on the home page (home,apps,support,blog,contact,about)
- No text in images
- Style sheet

Looks we like:
- http://x7k3lmq9pwrtzv.pixelmoorvault.net/412_Zelto_Site/final_large.jpg
- http://x7k3lmq9pwrtzv.pixelmoorvault.net/Premium_71_Illustrative_Korvix_Landing_Page/final.jpg
- http://grelmwick.com/
- http://dorniply.ca/
- http://quatzel.com/

Industry/Entity Type

Business

Requirements
Must have
• - Company logo should look great on pages.
• - Main home page and app landing page.
• - Section links/tabs on the home page (home,apps,support,blog,contact,about)
• - Web 2.0 style.
• - 960 grid system (12 col, 16 col).
• - Sliced ann optmized
• - Exported in all major formats (psd,ai,eps,png,jpeg,etc)
• - Style sheet
Should not have
• - Text in images

```html
<!DOCTYPE html>
<html lang="en">
<head>
<meta charset="utf-8">
<title>Plumweave — Download apps with a tap</title>
<link rel="stylesheet" href="https://fonts.googleapis.com/css2?family=Arimo:wght@400;700&display=swap">
<style>
:root{
  --bg:#262626;
  --bg-dark:#1d1d1d;
  --hero:#3a3a3a;
  --red:#d3141b;
  --red-dark:#9e0c10;
  --heading-red:#e0161c;
  --text:#ffffff;
  --muted:#6d6d6d;
  --line:#4a4a4a;
}
*{margin:0;padding:0;box-sizing:border-box}
html,body{width:1032px;height:1200px;overflow:hidden;background:var(--bg)}
body{font-family:"Arimo",Arial,sans-serif;color:var(--text)}
.page{position:relative;width:1032px;height:1200px;background:var(--bg);overflow:hidden}
.abs{position:absolute}

/* header */
.site-header{left:0;top:0;width:1032px;height:122px;background:linear-gradient(#2c2c2c,#232323);border-bottom:2px solid #161616}
.brand{display:flex;align-items:center;gap:10px;font-size:38px;font-weight:700;color:var(--text);letter-spacing:-.5px;white-space:nowrap}
.brand-dot{width:16px;height:16px;border-radius:50%;background:var(--red)}
.site-header .brand{left:22px;top:34px}
.main-nav{right:12px;top:34px;display:flex;align-items:center;gap:17px;font-size:19px}
.main-nav a{color:var(--text);text-decoration:none}

/* hero */
.hero{left:0;top:124px;width:1032px;height:458px;background:radial-gradient(ellipse at 70% 10%,#474747,var(--hero) 60%,#303030);border-bottom:3px solid #161616}
.hero-title{left:34px;top:44px;font-size:25px;font-weight:700;color:var(--heading-red);white-space:nowrap}
.hero-copy{left:34px;top:88px;width:410px;font-size:15px;line-height:21.5px}
.btn-demo{left:34px;top:308px;width:258px;height:52px}
.btn-demo span{position:absolute;left:16px;top:13px;font-size:23px;font-weight:700;color:var(--text);white-space:nowrap}
.tagline{left:496px;top:344px;transform:rotate(-90deg);transform-origin:0 0;font-size:29px;white-space:nowrap}
.tagline b{color:var(--red);font-weight:700}
.device-art{left:532px;top:30px;width:422px;height:410px;border-radius:30px;background:radial-gradient(ellipse at 50% 40%,#4d4d4d,#1a1a1a 70%)}
.slider-dots{left:978px;top:186px;width:20px;height:100px;background:#2a2a2a;border-radius:3px;display:flex;flex-direction:column;align-items:center;gap:4px;padding-top:10px}
.slider-dots i{width:8px;height:9px;background:#ddd;display:block}
.slider-dots i.on{background:var(--red)}

/* app strip */
.app-strip{left:14px;top:606px;width:994px;height:119px;border:1px solid #555;background:var(--bg)}
.app-item{display:flex;align-items:center;gap:10px;font-size:13px;line-height:19px;top:22px;white-space:nowrap}
.app-icon{width:60px;height:60px;border-radius:10px;flex:none}
.apps-tag{left:940px;top:595px;width:80px;height:80px;background:linear-gradient(var(--red),var(--red-dark));border:2px solid #fff3;display:flex;flex-direction:column;align-items:center;justify-content:flex-end;padding-bottom:8px;font-size:22px;font-weight:700}
.pager{left:466px;top:712px;width:112px;height:20px;background:linear-gradient(var(--red),var(--red-dark));display:flex;gap:4px;align-items:center;justify-content:center}
.pager i{width:9px;height:9px;background:#7a0a0d;display:block}
.pager i.on{background:#fff}

/* columns */
.info-columns{left:0;top:0;width:1032px;height:1200px;pointer-events:none}
.info-columns a{pointer-events:auto}
.col-title{font-size:25px;font-weight:700;color:var(--heading-red);white-space:nowrap}
.col-copy{font-size:13px;line-height:21.5px;width:262px}
.btn-small{width:102px;height:26px;background:linear-gradient(var(--red),var(--red-dark));border:1px solid #ff5a5a55;font-size:14px;font-weight:700;text-align:center;line-height:24px;color:#fff;text-decoration:none}
.mail-label{font-size:19px;white-space:nowrap}
.mail-input{left:746px;top:878px;width:264px;height:54px;background:radial-gradient(ellipse,#fff 40%,#cfcfcf);border:1px solid #999}
.btn-submit{left:908px;top:946px;width:101px;height:43px;background:linear-gradient(var(--red),var(--red-dark));border:1px solid #ff5a5a55;font-size:22px;font-weight:700;text-align:center;line-height:41px;color:#fff;text-decoration:none}

/* footer */
.footer-rule{left:14px;top:1084px;width:1004px;height:6px;background:repeating-linear-gradient(90deg,#3d3d3d 0 2px,transparent 2px 4px)}
.site-footer .brand{left:22px;top:1115px;font-size:32px}
.copyright{right:14px;top:1124px;font-size:12px;color:var(--muted);white-space:nowrap}
</style>
</head>
<body>
<div class="page">

  <header class="site-header abs">
    <div class="brand abs"><span class="brand-dot"></span>Plumweave</div>
    <nav class="main-nav abs">
      <a href="#" aria-label="Home">
        <svg width="40" height="36" viewBox="0 0 40 36"><path d="M20 2 L38 18 H32 V34 H8 V18 H2 Z" fill="#fff"/><rect x="16" y="22" width="8" height="12" fill="#d3141b"/></svg>
      </a>
      <a href="#">About</a><a href="#">Apps</a><a href="#">Support</a><a href="#">Blog</a><a href="#">Contact</a>
    </nav>
  </header>

  <section class="hero abs">
    <h1 class="hero-title abs">Download apps with a tap.</h1>
    <p class="hero-copy abs">Lorem ipsum dolor sit amet, consectetur adipiscing elit. Nulla magna odio, imperdiet et ullamcorper et, tempus non urna. Aliquam dictum orci non quam laoreet ac sagittis augue vestibulum. Nunc hendrerit feugiat iaculis. Praesent aliquam, felis eget blandit auctor, metus diam ultricies elit, id consequat justo dui non dui. Cras at lorem semper mi mollis euismod. Nulla augue risus, malesuada ac pellentesque nec, placerat eget enim.</p>
    <a class="btn-demo abs" href="#">
      <svg width="258" height="52" viewBox="0 0 258 52"><defs><linearGradient id="demoFill" x1="0" y1="0" x2="0" y2="1"><stop offset="0" stop-color="#e51a20"/><stop offset="1" stop-color="#a80d12"/></linearGradient></defs><path d="M1 1 H240 L257 26 L240 51 H1 Z" fill="url(#demoFill)" stroke="#ff6a6a" stroke-opacity=".4"/></svg>
      <span>Download for Demo</span>
    </a>
    <div class="tagline abs">Media to <b>Mobile</b></div>
    <div class="device-art abs" role="img" aria-label="Three Korvix phones showing app home screens"></div>
    <div class="slider-dots abs"><i></i><i></i><i></i><i></i><i></i><i class="on"></i></div>
  </section>

  <section class="app-strip abs">
    <div class="app-item abs" style="left:12px"><div class="app-icon" role="img" aria-label="Family app icon" style="background:linear-gradient(#8bb8d8,#c98a5a)"></div>Apps for Moms<br>and Dads</div>
    <div class="app-item abs" style="left:186px"><div class="app-icon" role="img" aria-label="Money app icon" style="background:linear-gradient(#9fd0e8,#6aa8c6)"></div>Apps for Managing<br>Money</div>
    <div class="app-item abs" style="left:381px"><div class="app-icon" role="img" aria-label="Timer app icon" style="background:linear-gradient(#555,#222)"></div>Apps for Work</div>
    <div class="app-item abs" style="left:547px"><div class="app-icon" role="img" aria-label="News app icon" style="background:linear-gradient(#6a6a6a,#1a1a1a)"></div>Apps for Keeping<br>Current</div>
    <div class="app-item abs" style="left:735px"><div class="app-icon" role="img" aria-label="Music app icon" style="background:linear-gradient(#fafafa,#dcdcdc)"></div>Apps for Music</div>
  </section>
  <div class="apps-tag abs">
    <svg width="22" height="34" viewBox="0 0 22 34"><rect x="1" y="1" width="20" height="32" rx="3" fill="#fff"/><rect x="4" y="5" width="14" height="21" fill="#d3141b"/><circle cx="11" cy="29.5" r="1.8" fill="#d3141b"/></svg>
    Apps
  </div>
  <div class="pager abs"><i class="on"></i><i></i><i></i><i></i><i></i><i></i></div>

  <section class="info-columns abs">
    <svg class="abs" style="left:20px;top:798px" width="40" height="40" viewBox="0 0 40 40"><circle cx="20" cy="20" r="15" fill="none" stroke="#fff" stroke-width="8"/><path d="M20 5 A15 15 0 0 1 35 20" fill="none" stroke="#d3141b" stroke-width="8"/><path d="M20 35 A15 15 0 0 1 5 20" fill="none" stroke="#d3141b" stroke-width="8"/></svg>
    <h2 class="col-title abs" style="left:73px;top:794px">Get Help</h2>
    <p class="col-copy abs" style="left:73px;top:834px">Suspendisse euismod velit sit amet justo pellentesque a facilisis ante venenatis. Donec lectus arcu, interdum nec ornare sed, cursus id augue. Maecenas mi tellus, placerat a fringilla vel, tristique fringilla sapien. Vestibulum ante ipsum primis in faucibus orci luctus et ultrices posuere cubilia Curae; Nunc eu felis ante.</p>
    <a class="btn-small abs" href="#" style="left:73px;top:1014px">Read more</a>

    <svg class="abs" style="left:362px;top:796px" width="56" height="40" viewBox="0 0 56 40"><ellipse cx="20" cy="20" rx="18" ry="11" fill="#eee"/><path d="M14 28 L10 38 L22 29 Z" fill="#eee"/><ellipse cx="38" cy="13" rx="16" ry="10" fill="#d3141b"/></svg>
    <h2 class="col-title abs" style="left:425px;top:794px">Read the blog</h2>
    <p class="col-copy abs" style="left:425px;top:834px;width:232px">Guspendisse euismod velit sit amet justo uellentesque a facilisis ante venenatis. Donec jectus arcu, interdum nec ornare sed, cursus id augue. Maecenas mi tellus, placerat a fringilla rfel, tristique fringilla sapien. Vestibulum ante ipsum primis in faucibus orci luctus et ultrices posuere cubilia Curae.</p>
    <a class="btn-small abs" href="#" style="left:425px;top:1015px">Read more</a>

    <svg class="abs" style="left:690px;top:790px" width="48" height="40" viewBox="0 0 48 40"><rect x="2" y="8" width="30" height="20" fill="#eee"/><path d="M2 8 L17 20 L32 8" fill="none" stroke="#999" stroke-width="1.5"/><path d="M24 22 H38 V16 L47 26 L38 36 V30 H24 Z" fill="#d3141b"/><circle cx="27" cy="6" r="6" fill="#d3141b"/></svg>
    <h2 class="col-title abs" style="left:749px;top:790px">Want the latest new?</h2>
    <p class="mail-label abs" style="left:749px;top:836px">Join our mailing list!</p>
    <div class="mail-input abs" role="textbox" aria-label="Email address"></div>
    <a class="btn-submit abs" href="#">Submit</a>
  </section>

  <div class="footer-rule abs"></div>
  <footer class="site-footer">
    <div class="brand abs"><span class="brand-dot"></span>Plumweave</div>
    <p class="copyright abs">©2010 Plumweave. All Rights Reserved</p>
  </footer>

</div>
</body>
</html>
```